Workout book cover design: Looking for Simple Classic Cover

I need a book cover design for "The Steady Middle". A book on exercises to strengthen the pelvic floor. Basically it's exercises for your torso and hips. I want something tasteful and classic looking.

I like this book cover design: http://www.pagelorn-books.example/Calm-Starters-Gentle-Routines-Ease-ebook/dp/Q93KX7TM41/ref=sr_1_40?ie=UTF8&qid=2958173306&sr=8-40&keywords=exercise+books

Book Title: The Steady Middle
Description to go under title: I'm working on that now and will have ready by the end of the project. (The hidden world of pelvic floor training. Discover the best exercises for creating a strong core, hips and pelvis today!)

Target Market(s)

Mostly women 35-65 and men 60+

Industry/Entity Type

Health And Wellness

Requirements
Must have
• ebook dementions: 1536 x 2048 I think works for all the online publishing companies
• 8x10 for print
Nice to have
• I like this book cover design: http://www.pagelorn-books.example/Calm-Starters-Gentle-Routines-Ease-ebook/dp/Q93KX7TM41/ref=sr_1_40?ie=UTF8&qid=2958173306&sr=8-40&keywords=exercise+books
• This cover is also ok, but no shiny. http://www.pagelorn-books.example/Bedrock-Renew-The-Climb-Poise/dp/4827305519/ref=sr_1_2?ie=UTF8&qid=2958176642&sr=8-2&keywords=foundation+book
Should not have
• I do not like this cover, it's crowded. http://www.pagelorn-books.example/Gym-Drills-Selfweight-flexing-drills-ebook/dp/Q71RWJZNHE/ref=sr_1_2?ie=UTF8&qid=2958174418&sr=8-2&keywords=workout+books
• I do not want anyone on the cover making eye contact.

```html
<!DOCTYPE html>
<html lang="en">
<head>
<meta charset="utf-8">
<title>The Steady Middle — Book Cover</title>
<link rel="stylesheet" href="https://fonts.googleapis.com/css2?family=Montserrat:wght@400;700&family=Antonio:wght@100;200&family=Josefin+Sans:wght@300&family=Libre+Baskerville:ital@0;1&display=swap">
<style>
  :root {
    --stage: #e9e6ee;
    --cream: #fbf7e6;
    --rose: #b9686a;
    --ink-soft: #7d7a72;
    --grey-light: #a9a7a2;
    --teal: #4fdad6;
    --teal-band: #79e8e0;
    --white: #ffffff;
  }
  * { box-sizing: border-box; margin: 0; padding: 0; }
  html, body { width: 1200px; height: 1200px; overflow: hidden; }
  body {
    background: var(--stage);
    display: flex;
    align-items: center;
    justify-content: center;
  }
  .cover {
    position: relative;
    width: 840px;
    height: 1100px;
    background: var(--cream);
    box-shadow: 0 10px 40px rgba(60, 50, 80, 0.18);
    overflow: hidden;
    text-align: center;
  }
  .cover__kicker {
    margin-top: 34px;
    font-family: "Montserrat", sans-serif;
    font-weight: 700;
    font-size: 25px;
    line-height: 1.2;
    letter-spacing: 3px;
    color: var(--rose);
    text-transform: uppercase;
  }
  .cover__promise {
    margin: 10px auto 0;
    width: 700px;
    font-family: "Montserrat", sans-serif;
    font-weight: 400;
    font-size: 15px;
    line-height: 1.3;
    color: var(--ink-soft);
    text-transform: uppercase;
    letter-spacing: -0.2px;
  }
  .cover__title-lead {
    margin-top: 22px;
    font-family: "Josefin Sans", sans-serif;
    font-weight: 300;
    font-size: 50px;
    letter-spacing: 18px;
    color: var(--grey-light);
    line-height: 1;
  }
  .cover__title-main {
    margin-top: 4px;
    font-family: "Antonio", sans-serif;
    font-weight: 100;
    font-size: 262px;
    line-height: 0.95;
    letter-spacing: 6px;
    color: var(--teal);
  }
  .cover__subtitle {
    margin-top: 10px;
    font-family: "Libre Baskerville", serif;
    font-style: italic;
    font-size: 29px;
    color: var(--ink-soft);
    line-height: 1.2;
  }
  .cover__description {
    margin-top: 8px;
    font-family: "Libre Baskerville", serif;
    font-style: italic;
    font-size: 17px;
    color: var(--ink-soft);
  }
  .cover__divider {
    display: block;
    margin: 16px auto 0;
  }
  .cover__photo {
    position: absolute;
    left: 0;
    right: 0;
    top: 580px;
    height: 432px;
    background:
      linear-gradient(to bottom, var(--cream) 0%, rgba(251, 247, 230, 0) 14%),
      radial-gradient(ellipse 38% 30% at 52% 18%, rgba(255, 244, 205, 0.95) 0%, rgba(250, 200, 150, 0.55) 45%, rgba(250, 200, 150, 0) 100%),
      linear-gradient(to bottom, #8f7a5a 0%, #7a5c58 35%, #5b4250 65%, #8b6f6e 85%, #b79a86 100%);
  }
  .cover__band {
    position: absolute;
    left: 0;
    right: 0;
    bottom: 0;
    height: 88px;
    background: var(--teal-band);
    display: flex;
    align-items: center;
    justify-content: center;
  }
  .cover__author {
    font-family: "Libre Baskerville", serif;
    font-size: 19px;
    letter-spacing: 3px;
    color: var(--white);
    text-transform: uppercase;
  }
</style>
</head>
<body>
  <main class="cover">
    <header class="cover__header">
      <h2 class="cover__kicker">The perfect pelvic floor training for<br>men and women</h2>
      <p class="cover__promise">The exercises are gentle and safe. They're also fun to do and easy to fit into your daily routine, and the success is immediate.</p>
    </header>

    <h1 class="cover__title">
      <span class="cover__title-lead" style="display:block">The Steady</span>
      <span class="cover__title-main" style="display:block">MIDDLE</span>
    </h1>

    <p class="cover__subtitle">The hidden world of pelvic floor training.</p>
    <p class="cover__description">Discover the best exercises for creating a strong core, hips and pelvis today!</p>

    <svg class="cover__divider" width="22" height="22" viewBox="0 0 22 22" aria-hidden="true">
      <rect x="5" y="5" width="12" height="12" fill="#b9b6ae" transform="rotate(45 11 11)"/>
    </svg>

    <div class="cover__photo" role="img" aria-label="Photograph of a woman with long fair hair seen from behind, sitting on a rock above a lake at sunset, with wooded hills and bright sun glare"></div>

    <footer class="cover__band">
      <span class="cover__author">Book Author</span>
    </footer>
  </main>
</body>
</html>
```